The Velvet Heron Espresso Nook Coffee Card

would like a coffee card designed for our café. Most cards are so boring and I need to stand out from the crowd (The Velvet Heron ). I require our logo on one side or the business name also a place for people to write their name and mobile number (collecting data base) and on the back the following
customer gets a stamp for the 1st three coffees purchased, on the 3rd one they get a free upsize. another 2 stamps and on the 3rd one (6) gets a free coffee, another 2 stamps and the customer gets another upsize (9th coffee purchased) and on the 10th card they recivie a voucher for a free pizza.
small print | one free pizza for dinner dining (not available for takeaways and must book), Cant be used with any other offers, opts in to hear from the herd if there is a deal on. cant trade for cash or gift

```html
<!DOCTYPE html>
<html lang="en">
<head>
<meta charset="utf-8">
<title>The Velvet Heron Espresso Nook – Coffee Card</title>
<link rel="stylesheet" href="https://fonts.googleapis.com/css2?family=Lato:ital,wght@0,300;0,400;1,400&family=Oswald:wght@500&display=swap">
<style>
  :root {
    --backdrop: #8e8e8e;
    --card: #231f20;
    --ink-light: #ececec;
    --ink-soft: #d9d9d9;
    --label-grey: #8c8c8c;
    --field: #cdcbcc;
    --mark: #dfe2e1;
    --rule: #8a8a8a;
  }
  * { margin: 0; padding: 0; box-sizing: border-box; }
  html, body {
    width: 1200px; height: 1200px; overflow: hidden;
    background: var(--backdrop);
  }
  .canvas { position: relative; width: 1200px; height: 1200px; }

  .card {
    position: absolute; top: 310px; height: 594px;
    background: var(--card);
    box-shadow: 2px 3px 6px rgba(0,0,0,0.35);
  }
  .card--front { left: 234px; width: 364px; }
  .card--back  { left: 627px; width: 370px; }

  /* Front */
  .brand-dot {
    position: absolute; left: 132px; top: 90px;
    width: 100px; height: 100px; border-radius: 50%;
    background: var(--mark);
  }
  .brand-name {
    position: absolute; left: 46px; top: 212px;
    width: 272px; height: 62px; overflow: visible;
  }
  .brand-name text {
    font-family: "Oswald", sans-serif; font-weight: 500;
    font-size: 54px; fill: #ffffff;
  }
  .brand-rule {
    position: absolute; left: 46px; width: 272px; top: 277px;
    border-top: 1px solid var(--rule);
  }
  .brand-tagline {
    position: absolute; left: 46px; width: 272px; top: 284px;
    font-family: "Lato", sans-serif; font-weight: 300; font-size: 15px; text-align: center;
    color: var(--ink-soft); text-transform: uppercase; letter-spacing: 0.3px;
  }
  .field-label {
    position: absolute; left: 28px;
    font-family: "Oswald", sans-serif; font-weight: 500;
    font-size: 29px; line-height: 32px; color: var(--label-grey);
    text-transform: uppercase; transform: scaleX(0.86); transform-origin: left;
  }
  .field-label--name { top: 352px; }
  .field-label--mobile { top: 461px; }
  .field-box {
    position: absolute; left: 26px; width: 311px; height: 46px;
    background: var(--field);
  }
  .field-box--name { top: 389px; }
  .field-box--mobile { top: 498px; }

  /* Back */
  .rewards {
    position: absolute; left: 28px; top: 108px; width: 312px;
    font-family: "Lato", sans-serif; font-size: 17px; line-height: 21.5px;
    letter-spacing: 0.1px; color: var(--ink-light);
  }
  .back-rule {
    position: absolute; left: 28px; width: 314px; top: 427px;
    border-top: 1px solid var(--rule);
  }
  .small-print {
    position: absolute; left: 29px; top: 441px; width: 292px;
    font-family: "Lato", sans-serif; font-style: italic;
    font-size: 14.5px; line-height: 19px; color: var(--ink-light);
  }
</style>
</head>
<body>
<main class="canvas">
  <section class="card card--front" aria-label="Card front">
    <div class="brand-dot" aria-hidden="true"></div>
    <svg class="brand-name" viewBox="0 0 272 62" role="img" aria-label="The Velvet Heron">
      <text x="0" y="55" textLength="272" lengthAdjust="spacingAndGlyphs">THE VELVET HERON</text>
    </svg>
    <div class="brand-rule"></div>
    <p class="brand-tagline">Espresso Nook</p>

    <p class="field-label field-label--name">Name</p>
    <div class="field-box field-box--name"></div>
    <p class="field-label field-label--mobile">Mobile</p>
    <div class="field-box field-box--mobile"></div>
  </section>

  <section class="card card--back" aria-label="Card back">
    <p class="rewards">
      Customer gets a stamp for the 1st three coffees purchased,<br>
      on the 3rd one they get a free upsize.<br>
      another 2 stamps and on the 3rd one (6) gets a free coffee,<br>
      another 2 stamps and the customer gets another upsize (9th coffee purchased)<br>
      and on the 10th card they recivie a voucher for a free pizza.
    </p>
    <div class="back-rule"></div>
    <p class="small-print">
      One free pizza for dinner dining (not available for takeaways and must book),<br>
      Cant be used with any other offers, opts<br>
      in to hear from<br>
      the herd if there is a deal on.<br>
      Cant trade for cash or gift
    </p>
  </section>
</main>
</body>
</html>
```